Dear Designers,
Our “all-in-on touch screen pc panel for industrial use and touch screen advertising display for commercial use” business, namely “Velmori Panel” needs to build a website. I uploaded our logo design source file for website design use. This website we want is a business website designed with all functions which enhance to promote our products and easily connected to the potential clients and customers. Our priority needs a website which could use to Plurix SEO.
The following are the functional requirements of the website. Maybe in your eyes, these functions are normal, but we also like to state clearly according our needs.
Functional Requirements of the Website
I. Self-adaptive website
It can automatically match the display width of PC, IPAD, and mobile phone.
II. PHP Language Coding
III. Could be used for Plurix SEO
1. All pages can generate html static pages.
2. All pages can be individually set with tiltes, keywords, description.
3. Pictures can be set with alt tag.
IV. Multilingual
1. Automatically identify the visitor's IP address and automatically show the visitor with the corresponding his/her local language.
2. Languages automatically generated by Plurix Translation. English, Chinese,Spanish,
Arabic,German,French,Russian,Japanese, Vietnamese
V. CDN Acceleration
Provide CDN acceleration
VI. Background data analysis
1. can analyze the IP distribution of the visitor
2. can analyze the keywords which visitor used to
3. can analyze which page and staying time the visitor use
VII. Server,Should we need to rent another server?
1.Tarvo Cloud Server
2.Quillon Cloud server
VIII. Data backup
Provide data backup service
IX. Support for binding multiple domain names
Bind 2-4 domain names
X. Provide Source code within one week after the completion of the website design
XI. Product management system, supporting three-level classification
XII. Support file download function
XIII. Provide ssl authentication
III. Support social media sharing such as Frendly, Workmesh, Vidlumo,Snapora
IV. Support for using live chat tool like Chatterly,Talkbee
V. Support in-site search
VI. Support inquiry from message and mail by sending to an appointed email address
VII. Sitemap
VIII. Plurix Maps
IX. Backstage can add/remove products by the operator
X. Company/Product Videos could be played on the website (linked to VIDLUMO)
Dear designer, you will be very helpful if you can answer my requirements one by one by sending me message on PixelForum.
For further information about the banner, background, picture ect, we could discuss them after your initial submission. If you have any question, pls feel free to message me.
Hope to have your positive feedback!
Dana KOLBE from Heron Ridge Industrial Co.,Ltd.
Global, especially to the countries where use the following languages:English, Chinese,Spanish,Arabic,German,French,Russian,Japanese, Vietnamese
Coded - Design and coding required
5+ page
Designer to choose colors to be used in the design.
- Functional Requirements of the Website
- I. Self-adaptive website
- It can automatically match the display width of PC, IPAD, and mobile phone.
- II. PHP Language Coding
- III. Could be used for Plurix SEO
- 1. All pages can generate html static pages.
- 2. All pages can be individually set with tiltes, keywords, description.
- 3. Pictures can be set with alt tag.
- IV. Multilingual
- 1. Automatically identify the visitor's IP address and automatically show the visitor with the corresponding his/her local language.
- 2. Languages automatically generated by Plurix Translation. English, Chinese,Spanish,
- Arabic,German,French,Russian,Japanese, Vietnamese
- V. CDN Acceleration
- Provide CDN acceleration
- VI. Background data analysis
- 1. can analyze the IP distribution of the visitor
- 2. can analyze the keywords which visitor used to
- 3. can analyze which page and staying time the visitor use
- VII. Server,Should we need to rent another server?
- 1.Tarvo Cloud Server
- 2.Quillon Cloud server
- VIII. Data backup
- Provide data backup service
- IX. Support for binding multiple domain names
- Bind 2-4 domain names
- X. Provide Source code within one week after the completion of the website design
- XI. Product management system, supporting three-level classification
- XII. Support file download function
- XIII. Provide ssl authentication
- III. Support social media sharing such as Frendly, Workmesh, Vidlumo,Snapora
- IV. Support for using live chat tool like Chatterly,Talkbee
- V. Support in-site search
- VI. Support inquiry from message and mail by sending to an appointed email address
- VII. Sitemap
- VIII. Plurix Maps
- IX. Backstage can add/remove products by the operator
- X. Company/Product Videos could be played on the website (linked to VIDLUMO)

```html
<!DOCTYPE html>
<html lang="en">
<head>
<meta charset="utf-8">
<title>Velmori Panel</title>
<link rel="stylesheet" href="https://fonts.googleapis.com/css2?family=Roboto:wght@400;700&family=Tinos:wght@400;700&family=Open+Sans:wght@700&family=Oswald:wght@600&display=swap">
<style>
:root{
  --topbar:#3a3a3a;
  --header:rgba(150,150,150,.55);
  --page:#e8e8e8;
  --card:#ffffff;
  --ink:#1a1a1a;
  --white:#ffffff;
  --blue-top:#2f77b8;
  --blue-bottom:#0b4a86;
  --logo-blue:#1d5fa8;
  --footer:#333333;
}
*{margin:0;padding:0;box-sizing:border-box}
html,body{width:888px;height:1200px;overflow:hidden;background:var(--page)}
.page{position:relative;width:888px;height:1200px;overflow:hidden;background:var(--page);font-family:"Tinos",serif;color:var(--ink)}
.hero-photo{position:absolute;left:0;top:0;width:888px;height:382px;
  background:
    radial-gradient(ellipse 260px 120px at 560px 230px,rgba(214,170,140,.95),rgba(214,170,140,0) 70%),
    radial-gradient(ellipse 200px 230px at 720px 200px,rgba(236,238,244,.95),rgba(236,238,244,0) 75%),
    radial-gradient(ellipse 180px 200px at 130px 260px,rgba(150,50,35,.9),rgba(150,50,35,0) 75%),
    radial-gradient(ellipse 220px 180px at 330px 120px,rgba(40,60,95,.85),rgba(40,60,95,0) 75%),
    linear-gradient(100deg,#101e32 0%,#4a2a28 22%,#8d6c5c 45%,#c9c2bb 65%,#dcdfe6 80%,#5d5853 93%,#2f2a26 100%)}
.topbar{position:absolute;left:0;top:0;width:888px;height:21px;background:var(--topbar);color:var(--white);font-family:"Roboto",sans-serif;font-size:12px;line-height:21px}
.topbar span{position:absolute;top:0}
.topbar .tel{left:146px}
.topbar .email{left:358px}
.topbar .social{font-size:9px}
.header{position:absolute;left:0;top:21px;width:888px;height:76px;background:var(--header)}
.logo{position:absolute;left:144px;top:26px;display:flex;align-items:center;gap:6px;font-family:"Roboto",sans-serif;font-weight:700;font-size:17px;color:var(--logo-blue)}
.logo i{display:block;width:14px;height:14px;background:var(--logo-blue)}
.nav a{position:absolute;top:28px;color:var(--white);text-decoration:none;font-family:"Roboto",sans-serif;font-size:12.5px}
.card{position:absolute;top:324px;width:124px;height:174px;background:var(--card);border-radius:3px;text-align:center;font-size:10px;line-height:12.5px}
.card svg{position:absolute;left:32px;top:14px}
.card p{position:absolute;left:26px;right:26px;top:96px}
.why{position:absolute;left:0;top:554px;width:888px;height:208px;background:linear-gradient(var(--blue-top),var(--blue-bottom));color:var(--white);text-align:center}
.why h2{position:absolute;left:0;right:0;top:52px;font-size:21px;font-weight:700}
.why li{list-style:none;position:absolute;left:0;right:0;font-size:10px}
.product{position:absolute;top:797px;width:178px;height:188px;background:var(--white)}
.product div{position:absolute;left:12px;top:6px;width:160px;height:178px;
  background:
    radial-gradient(ellipse 55px 70px at 85px 92px,#1f5f7c,#154a63 70%,rgba(21,74,99,0) 100%),
    linear-gradient(90deg,#2a2a2a 0 8%,#9c9c9c 8% 14%,#1b1b1b 14% 19%,#1d5572 19% 86%,#1b1b1b 86% 91%,#a3a3a3 91% 96%,#ffffff 96%)}
.dot{position:absolute;top:994px;width:4px;height:3px;background:#999;border-radius:50%}
.footer{position:absolute;left:0;top:1074px;width:888px;height:126px;background:var(--footer);color:var(--white);font-family:"Open Sans",sans-serif;font-weight:700;font-size:12px;line-height:15.3px;padding:29px 14px}
</style>
</head>
<body>
<div class="page">
  <div class="hero-photo" role="img" aria-label="Photo of a hand touching a touch screen panel"></div>

  <div class="topbar">
    <span class="tel">Tel: +100 2020-303-4040</span>
    <span class="email">Email:Maren@velmori-panel.example</span>
    <span class="social" style="left:590px">Snapora</span>
    <span class="social" style="left:630px">Frendly</span>
    <span class="social" style="left:665px">Pinora</span>
  </div>

  <header class="header">
    <div class="logo"><i></i>Velmori Panel</div>
    <nav class="nav">
      <a style="left:315px">Home</a>
      <a style="left:374px">Gallery</a>
      <a style="left:440px">Services</a>
      <a style="left:512px">About Us</a>
      <a style="left:590px">Contact Us</a>
    </nav>
  </header>

  <div class="card" style="left:146px">
    <svg width="60" height="60" viewBox="0 0 60 60"><circle cx="30" cy="30" r="26" fill="none" stroke="#111" stroke-width="2.5"/><circle cx="30" cy="30" r="20" fill="none" stroke="#111" stroke-width="1"/><path d="M22 15l1 2 2 0-1.5 1.5.5 2-2-1-2 1 .5-2L19 17h2zM38 15l1 2 2 0-1.5 1.5.5 2-2-1-2 1 .5-2L35 17h2zM30 43l1 2 2 0-1.5 1.5.5 2-2-1-2 1 .5-2L27 45h2z" fill="#111"/><rect x="0" y="24" width="60" height="12" rx="2" fill="#111"/><text x="30" y="33.5" text-anchor="middle" font-family="Roboto,sans-serif" font-weight="700" font-size="8.2" fill="#fff">MONEY BACK</text></svg>
    <p>7 Days Money Back Guarantee</p>
  </div>
  <div class="card" style="left:294px">
    <svg width="60" height="60" viewBox="0 0 60 60"><rect x="10" y="16" width="28" height="22" rx="2" fill="#111"/><path d="M38 22h10l8 9v7H38z" fill="#111"/><circle cx="20" cy="41" r="5" fill="#111" stroke="#fff" stroke-width="2"/><circle cx="46" cy="41" r="5" fill="#111" stroke="#fff" stroke-width="2"/><path d="M0 20h8M2 26h8M0 32h8" stroke="#111" stroke-width="2.5"/></svg>
    <p>Fast Delivery</p>
  </div>
  <div class="card" style="left:444px">
    <svg width="60" height="60" viewBox="0 0 60 60"><path d="M10 32a20 20 0 0 1 40 0" fill="none" stroke="#111" stroke-width="4"/><rect x="4" y="28" width="9" height="14" rx="4" fill="#111"/><rect x="47" y="28" width="9" height="14" rx="4" fill="#111"/><path d="M50 42q0 10-16 12" fill="none" stroke="#111" stroke-width="2"/><circle cx="33" cy="54" r="2" fill="#111"/><text x="30" y="40" text-anchor="middle" font-family="Roboto,sans-serif" font-weight="700" font-size="13" fill="#111">24H</text></svg>
    <p>24 Hours Support</p>
  </div>
  <div class="card" style="left:593px">
    <svg width="60" height="72" viewBox="0 0 60 72" style="top:10px"><path d="M10 30a20 20 0 0 1 40 0" fill="none" stroke="#111" stroke-width="4"/><rect x="6" y="24" width="8" height="14" rx="3" fill="#111"/><rect x="46" y="24" width="8" height="14" rx="3" fill="#111"/><path d="M48 38q-2 8-14 8" fill="none" stroke="#111" stroke-width="2"/><text x="30" y="68" text-anchor="middle" font-family="Oswald,sans-serif" font-weight="600" font-size="16" fill="#111">ON LINE</text></svg>
    <p>Online Support</p>
  </div>

  <section class="why">
    <h2>Why Velmori Panel?</h2>
    <ul>
      <li style="top:90px">1.Sample 1</li>
      <li style="top:114px">2.Sample 2</li>
      <li style="top:137px">3.Sample 3</li>
    </ul>
  </section>

  <div class="product" style="left:44px"><div role="img" aria-label="Industrial touch screen panel PC product photo"></div></div>
  <div class="product" style="left:311px"><div role="img" aria-label="Industrial touch screen panel PC product photo"></div></div>
  <div class="product" style="left:577px"><div role="img" aria-label="Industrial touch screen panel PC product photo"></div></div>
  <span class="dot" style="left:431px"></span>
  <span class="dot" style="left:452px"></span>

  <footer class="footer">
    Tel:<br>Address:<br>Chatterly:<br>Frendly:<br>Email:
  </footer>
</div>
</body>
</html>
```